New Toothpaste brand needs a logo & packaging design

Our company is launching a new toothpaste and is looking for a logo and packaging design. The toothpaste brand is called Brivana. The packaging should have the same design quality as the major international brands, such as Lumora, Lumora Totalcare, Dentiva, Pexolo, Wind-rise, Marvest, etc. The dominant colors for our brand should be hues of blue, similar to other major brands. In addition, there should be a little bit of green to represent the "Fresh Mint Blast" flavor and the "Extracts of Aloe Vera" included in the ingredients.

There are typically 3 unique sides on a toothpaste box:

The face: Repeated on ~3 sides of the 4 faces of the box
The back: The 4th box face has the instructions for use, ingredients, company information, bar code/product info, and some branding elements.
The sides: Usually consisting of just the logo, flavor etc.

Please refer to existing brands such as Lumora, Lumora Total-care, and Dentiva for an example of typical box layout and elements.

Task Details:
Package Dimensions: 180 mm x 48 mm x 28 mm, 100 ml toothpaste tube
Brand Name: Brivana
Description: Fluoride Toothpaste
Flavor: Fresh Mint Blast
5 Actions: Protects against cavities and tartar, freshens breath, whitens teeth, and maintains healthy gums. These actions can also be made into a list like Lumora Total Care or Dentiva Max care. For instance, Strong Teeth, Fresh Breath, Whitening, Healthy Gums, Cavity and Tartar Protection.
Also contains whitening micro particles and extracts of aloe vera which may be highlighted on the package

Overall, the look should be high quality and with the same look and feel as the big brands mentioned previously. We do not have an existing logo for this brand. The face of the package is the most important element as it is often repeated on several sides and on the tube itself.

Please let me know if you have any questions.

I've attached some of our favorite big brand designs below. I would say the Lumora Total Care and Gleam vers

The logos I've seen so far for Brivana, have been a bit too bold. A little bold is okay, but just needs to be moderate. 

I would like the colors to be bright and appealing. I mentioned shades of blue being the major color, but green should also be highlighted as well, perhaps in a 80% blue to 20% green ratio. 

Target Market(s)

adult consumer of toothpaste, both female and male.

Industry/Entity Type

It Company

Requirements
Must have
• A logo with the brand name: Brivana
Description or sub text: Fluoride Toothpaste
Flavor: Fresh Mint Blast
A phrase or list describing the Toothpaste Actions: e.g., Protects against cavities and tartar, freshens breath, whitens teeth, and maintains healthy gums. Or as a list simialr to Lumora Total Care or Dentiva Max Care:
-Anti-cavity
-Anti-tartar
-Fresh breath
-Whitening
-Healthy Gums

Special ingredient of "whitening micro particles: and "extracts of aloe vera", which should also be highlighted.

The color should mostly be shades of blue, with only a little bit of green to accentuate the fresh mint blast flavor and aloe vera

Nice to have
• The design should really look good next to lumora total care, gleam pure, and dentiva max care. These are our favorite designs.
Should not have
• For aloe vera, there is no need to show the plant.

The Brivana logo shouldn't be too Bold. This should be appeal to all consumers, not just men.

```html
<!DOCTYPE html>
<html lang="en">
<head>
<meta charset="utf-8">
<title>Brivana Fluoride Toothpaste – Box Panels</title>
<link rel="stylesheet" href="https://fonts.googleapis.com/css2?family=Roboto+Condensed:wght@300;400;700&display=swap">
<style>
  :root {
    --page: #ffffff;
    --sky-light: #e6f6fe;
    --sky: #8fd3f6;
    --ocean: #3fa6ec;
    --ocean-deep: #1f6fe8;
    --brand-blue: #1550c8;
    --ink-white: #ffffff;
    --ink-shadow: rgba(10, 50, 140, 0.55);
    --mint: #6fe21c;
    --mint-light: #d8ff3a;
    --mint-edge: #3fae10;
  }
  * { box-sizing: border-box; margin: 0; padding: 0; }
  html, body { width: 1200px; height: 1000px; overflow: hidden; background: var(--page); }
  body { position: relative; font-family: "Roboto Condensed", Arial, sans-serif; }

  .panel { position: absolute; overflow: hidden; }
  .panel--front-slim { left: 100px; top: 120px; width: 1008px; height: 157px; }
  .panel--front-tall { left: 100px; top: 336px; width: 1006px; height: 269px; }
  .panel--side { left: 470px; top: 691px; width: 268px; height: 157px; }

  .water {
    position: absolute; inset: 0;
    background:
      radial-gradient(ellipse 45% 70% at 32% 25%, rgba(255,255,255,0.95), rgba(255,255,255,0) 70%),
      radial-gradient(ellipse 30% 60% at 62% 70%, rgba(200,238,255,0.8), rgba(200,238,255,0) 70%),
      linear-gradient(100deg, var(--ocean) 0%, var(--sky) 18%, var(--sky-light) 38%, var(--sky) 65%, var(--ocean) 100%);
  }
  .actions-field {
    position: absolute; inset: 0;
    background: linear-gradient(160deg, var(--ocean-deep) 0%, var(--ocean) 55%, var(--sky) 100%);
    opacity: 0.9;
  }
  .panel--front-slim .actions-field { clip-path: polygon(86.5% 0, 100% 0, 100% 100%, 72.5% 100%); }
  .panel--front-tall .actions-field { clip-path: polygon(83% 0, 100% 0, 100% 100%, 60% 100%); }

  .brand-lockup { position: absolute; display: flex; flex-direction: column; }
  .brand-name {
    color: var(--brand-blue); font-weight: 700; letter-spacing: 0.04em; line-height: 1;
    display: flex; align-items: center;
  }
  .brand-dot { display: inline-block; border-radius: 50%; background: var(--brand-blue); margin-right: 0.2em; }
  .brand-sub {
    color: var(--ink-white); font-weight: 700; letter-spacing: 0.18em;
    text-shadow: 1px 1px 0 var(--ink-shadow);
  }

  .panel--front-slim .brand-lockup { left: 80px; top: 30px; }
  .panel--front-slim .brand-name { font-size: 56px; }
  .panel--front-slim .brand-dot { width: 18px; height: 18px; }
  .panel--front-slim .brand-sub { font-size: 13px; margin-top: 12px; margin-left: 50px; }

  .panel--front-tall .brand-lockup { left: 90px; top: 60px; }
  .panel--front-tall .brand-name { font-size: 100px; }
  .panel--front-tall .brand-dot { width: 30px; height: 30px; }
  .panel--front-tall .brand-sub { font-size: 20px; margin-top: 16px; margin-left: 95px; }

  .panel--side .brand-lockup { left: 28px; top: 46px; }
  .panel--side .brand-name { font-size: 42px; }
  .panel--side .brand-dot { width: 13px; height: 13px; }
  .panel--side .brand-sub { font-size: 11px; margin-top: 12px; margin-left: 18px; }

  .ingredients { position: absolute; color: var(--ink-white); letter-spacing: 0.16em; text-transform: uppercase; font-weight: 300; }
  .ingredients strong { font-weight: 700; text-shadow: 1px 1px 0 var(--ink-shadow); }
  .panel--front-slim .ingredients { left: 440px; top: 38px; width: 260px; text-align: center; font-size: 13px; line-height: 27px; }
  .panel--front-tall .ingredients { left: 66px; top: 230px; font-size: 15px; }

  .flavor-burst { position: absolute; }
  .panel--front-slim .flavor-burst { left: 731px; top: 27px; width: 124px; height: 124px; }
  .panel--front-tall .flavor-burst { left: 675px; top: 62px; width: 120px; height: 120px; }
  .flavor-burst svg { position: absolute; inset: 0; width: 100%; height: 100%; }
  .flavor-label {
    position: absolute; inset: 0; display: flex; flex-direction: column; align-items: center; justify-content: center;
    color: var(--ink-white); font-size: 14px; line-height: 1.05; text-align: center;
  }
  .flavor-label b { font-weight: 700; }

  .actions { position: absolute; color: var(--ink-white); list-style: none; text-transform: uppercase; }
  .actions-title { font-weight: 700; color: var(--ink-white); text-shadow: 1px 1px 0 var(--brand-blue), -1px -1px 0 var(--brand-blue); letter-spacing: 0.04em; }
  .actions li { position: relative; }
  .actions li::before {
    content: ""; position: absolute; border-radius: 50%;
    background: radial-gradient(circle, var(--ink-white) 35%, var(--sky) 40%, var(--ink-white) 75%);
  }
  .panel--front-slim .actions { left: 885px; top: 12px; font-size: 12px; line-height: 18.5px; }
  .panel--front-slim .actions-title { font-size: 15px; }
  .panel--front-slim .actions li { padding-left: 8px; }
  .panel--front-slim .actions li::before { left: 0; top: 6px; width: 6px; height: 6px; }
  .panel--front-tall .actions { left: 825px; top: 37px; font-size: 20px; line-height: 29.5px; }
  .panel--front-tall .actions-title { font-size: 24px; margin-bottom: 2px; }
  .panel--front-tall .actions li { padding-left: 14px; }
  .panel--front-tall .actions li::before { left: 0; top: 10px; width: 9px; height: 9px; }
</style>
</head>
<body>

  <section class="panel panel--front-slim">
    <div class="water" role="img" aria-label="Soft blue water ripple texture"></div>
    <div class="actions-field"></div>
    <div class="brand-lockup">
      <div class="brand-name"><span class="brand-dot"></span>BRIVANA</div>
      <div class="brand-sub">FLOURIDE TOOTHPASTE</div>
    </div>
    <p class="ingredients">Contains<br><strong>Whitening Micro Particles</strong><br>And extracts of <strong>Aloe Vera</strong></p>
    <div class="flavor-burst">
      <svg viewBox="-60 -60 120 120" aria-hidden="true">
        <defs>
          <radialGradient id="mintSlim"><stop offset="0" stop-color="#2fc40a"/><stop offset="0.7" stop-color="#7fe81e"/><stop offset="1" stop-color="#e4ff3a"/></radialGradient>
        </defs>
        <g fill="url(#mintSlim)">
          <rect x="-38" y="-38" width="76" height="76"/>
          <rect x="-38" y="-38" width="76" height="76" transform="rotate(15)"/>
          <rect x="-38" y="-38" width="76" height="76" transform="rotate(30)"/>
          <rect x="-38" y="-38" width="76" height="76" transform="rotate(45)"/>
          <rect x="-38" y="-38" width="76" height="76" transform="rotate(60)"/>
          <rect x="-38" y="-38" width="76" height="76" transform="rotate(75)"/>
        </g>
      </svg>
      <div class="flavor-label"><span>FRESH</span><b>MINT</b><span>BLAST</span></div>
    </div>
    <ul class="actions">
      <li class="actions-title">5 Actions</li>
      <li>Strong Teeth</li>
      <li>Fresh Breath</li>
      <li>Whitening</li>
      <li>Healthy Gums</li>
      <li>Cavity &amp; Tartar<br>Protection</li>
    </ul>
  </section>

  <section class="panel panel--front-tall">
    <div class="water" role="img" aria-label="Soft blue water ripple texture"></div>
    <div class="actions-field"></div>
    <div class="brand-lockup">
      <div class="brand-name"><span class="brand-dot"></span>BRIVANA</div>
      <div class="brand-sub">FLOURIDE TOOTHPASTE</div>
    </div>
    <p class="ingredients">Contains <strong>Whitening Micro Particles</strong> and extracts of <strong>Aloe Vera</strong></p>
    <div class="flavor-burst">
      <svg viewBox="-60 -60 120 120" aria-hidden="true">
        <defs>
          <radialGradient id="mintTall"><stop offset="0" stop-color="#2fc40a"/><stop offset="0.7" stop-color="#7fe81e"/><stop offset="1" stop-color="#e4ff3a"/></radialGradient>
        </defs>
        <g fill="url(#mintTall)">
          <rect x="-38" y="-38" width="76" height="76"/>
          <rect x="-38" y="-38" width="76" height="76" transform="rotate(15)"/>
          <rect x="-38" y="-38" width="76" height="76" transform="rotate(30)"/>
          <rect x="-38" y="-38" width="76" height="76" transform="rotate(45)"/>
          <rect x="-38" y="-38" width="76" height="76" transform="rotate(60)"/>
          <rect x="-38" y="-38" width="76" height="76" transform="rotate(75)"/>
        </g>
      </svg>
      <div class="flavor-label"><span>FRESH</span><b>MINT</b><span>BLAST</span></div>
    </div>
    <ul class="actions">
      <li class="actions-title">5 Actions</li>
      <li>Strong Teeth</li>
      <li>Fresh Breath</li>
      <li>Whitening</li>
      <li>Healthy Gums</li>
      <li>Cavity &amp; Tartar<br>Protection</li>
    </ul>
  </section>

  <section class="panel panel--side">
    <div class="water" role="img" aria-label="Soft blue water ripple texture"></div>
    <div class="brand-lockup">
      <div class="brand-name"><span class="brand-dot"></span>BRIVANA</div>
      <div class="brand-sub">FLOURIDE TOOTHPASTE</div>
    </div>
  </section>

</body>
</html>
```